Marketing / Informational Site for Marriage and Family Therapists Cooperative

We need a web design for a new Marriage and Family Therapist Cooperative, called Meadowgate Counselors. This is a market and information site for potential clients and referrals to learn more about the team and get contact information.

We are looking for profession, clean, and modern design, that cater towards families and mom's concerned about their families mental health and child development.

This should include a home page, an general about page, 3 bio pages (1 for each therapist listed below), and a general contact us page.

Our Domain Name

Meadowgatecounselors.example

Company Name

Meadowgate Counselors

Group Moto/Philosophy

“Our sorrows and wounds are healed only when we touch them with compassion.” - Orvelan

Our Logo

See Heron Final (attached)

Home Page (Introduction)

Feeling stressed and overwhelmed?
Encountering barriers towards your goals?
Having difficulty accomplishing the simplest task?
Have the need to talk but unsure who to turn to?

Therapy can assist you in overcoming all of these challenges. Assist you in uncovering the difficulties and barriers that are keeping you from achieving your life’s ambitions, help discover ways to overcome them, and cope with the impact your behaviour has on your occupation, personal life and social life.

Welcome to our practice, with over 20 years of combined experience in the clinical field you are sure to find the right fit for your needs. Each clinician has experience working with groups, adults, teens, children, families, and couples. We specialize in fostering healthy relationships between individuals, managing depression and anxiety, overcoming trauma, and developing occupational success. Feel free to explore information about each clinician and make an appointment with one of us today.

About Us (bio pics attached)

Marisel Dunkworth

My name is Dr. MariSel Dunkworth and I am a Licensed Marriage Family Therapist with a practice in Riverside, CA. I have devoted my life’s work into developing my skills in this profession. I have over 15 years of experience working in the clinical and the social service settings. These years have afforded me the opportunity to work with groups, families, adults, teens and children with varying symptoms. I have helped clients that have trauma, abuse histories, and many within the legal or social service systems. I enjoy working individuals from all walks of life achieve self sufficiency, social success and occupational success. In my years of training I have come to develop a culturally sensitive practice that centers around the needs of the client.

I have held many positions in my clinical career beginning as clinician moving upwards toward supervisor and program coordinator. I have also over 5 years of experience as an adjunct faculty member in the University setting teaching student to become Marriage and Family Therapists. As a clinician I focused on enriching my clinical skills by developing outcome driven practices to achieve client’s desired goals. As a clinical supervisor, I guided clinicians along their own paths towards clinical licensure. As a program coordinator, I helped develop a clinical assessment and triage program from ground up to assist client in accessing services in the South Los Angeles Area. The program would assist over 100 plus clients on a monthly basis get connected to clinical services and linked to any additional resources as needed by the individual. I have graduated with my, Bachelor’s degree at the Halvern College, Riverside. I received my Masters degree in Clinical Psychology at Mount St. Mary’s University, and my Doctorate degree in Clinical Psychology at Tamsworth Institute.

To schedule an appointment with Dr. MariSel Dunkworth, LMFT:

email: marisel582@postbox.example
Phone: (951)555-0182

Jeb Kowal

My name is Rosalindra (Jeb) Kowal, I received my Masters Degree of Counseling in Marriage and Family Therapy from Corvell Bay State College in June 2000. I have acquired over 15 years of experience helping Individuals, Couples, and Families cope with issues of Anxiety, Depression, Grief and Bereavement, and HIV/AIDS.

I am a Family Systems Therapist and I truly believe the dynamics in our family of origin greatly shape our current belief systems and behaviors. However, I often utilize a variety of approaches to help my clients achieve their goals depending on their individual needs.

My greatest strength as a Marriage and Family Therapist is helping my clients explore ways to make the changes in their lives that will allow them to live their life to their fullest potential. I help my clients achieve their personal life goals with a warm, safe, non-judgmental , and supportive environment. In doing so, my clients are encouraged to explore the issues that may be preventing them from living the life they desire. Thus, empowering them to take control of their personal journey to living a productive and meaningful life.

If you feel that you are ready to commit to bringing about positive changes in your life and would like support in exploring this path, I’m here to work with you in your journey to personal growth and development.

To schedule an appointment with Rosalindra Kowal, LMFT:

e-mail: rkjeb7@mailnest.example
Phone: (951)555-0147

Dena Holcroft

Dena Holcroft graduated with a Masters in Marriage and Family Therapy from Pellridge Crestwood College. She currently holds a license in Marriage and Family Therapy in the State of California. She is also formally trained in Clinical Art Therapy. Dena's expertise lies in providing treatment to individuals experiencing work-related injuries, severe physical and emotional pain, trauma, grief and loss, anxiety and depression. In her early career, she provided valuable service at the largest free clinic in the nation serving marginalized families and children. For the past ten years, Dena has worked with HIV/AIDS population.
Dena comes from a multicultural background and she has utilized this experience and knowledge in serving a variety of populations. At an organizational level, Dena has worked extensively with challenging issues such as the chemical dependency and homelessness. In her private practice, Dena is proficient in working within individuals experiencing relationship concerns, marital and family conflict, depression/anxiety, self-esteem concerns, adjustment disorders, and pain management. She has treated clients from diverse cultural, linguistic backgrounds and sexual orientations.
Dena is trained in Family Systems Theory and incorporates other strategies appropriate for each presenting issue. She specializes in Clinical Art Therapy and has successfully utilized an integrated approach including guided imagery and relaxation skills training for many years.

To schedule an appointment with Dena Holcroft, LMFT

e-mail: greypinestudio@inkmail.example
Phone: (951) 555-0169

Target Market(s)

Families with child development, marriage issues, or other mental health needs

Industry/Entity Type

Marketing

Number of Pages Required

5+ page

Requirements
Must have
• 1 home page, 1 about page, 1 contact page. About page could either be standalone page with 3 different bio pages for each therapist or an all in one about page that includes bios for all 3 therapists.

```html
<!DOCTYPE html>
<html lang="en">
<head>
<meta charset="utf-8">
<title>Meadowgate Counselors</title>
<link rel="stylesheet" href="https://fonts.googleapis.com/css2?family=Open+Sans:wght@400;600&display=swap">
<style>
  :root {
    --lime: #b3cb3c;
    --lime-light: #c9dc6a;
    --lime-text: #8cb321;
    --ink: #1f1f1f;
    --body-grey: #6f6f6f;
    --black: #0d0d0d;
    --white: #ffffff;
    --page: #fbfbf8;
  }
  * { box-sizing: border-box; margin: 0; padding: 0; }
  html, body { width: 870px; height: 1200px; overflow: hidden; }
  body {
    background: var(--page);
    font-family: "Open Sans", Arial, sans-serif;
    color: var(--ink);
    position: relative;
  }
  .hero {
    position: absolute; left: 0; top: 0; width: 870px; height: 580px;
    background: linear-gradient(135deg, #eef1ee 0%, #dfe4e2 35%, #c9b59c 55%, #a98a6c 75%, #6f8fa8 100%);
  }
  .brand {
    position: absolute; left: 40px; top: 48px;
    display: flex; align-items: center; gap: 10px;
  }
  .brand-dot { width: 34px; height: 34px; border-radius: 50%; background: var(--lime); }
  .brand-name { font-size: 20px; font-weight: 600; color: var(--lime-text); line-height: 1.15; width: 130px; }
  .main-nav {
    position: absolute; left: 232px; top: 44px; width: 478px; height: 50px;
    background: var(--lime); border-radius: 25px;
    display: flex; align-items: center; padding: 0 8px; gap: 8px;
  }
  .main-nav a {
    text-decoration: none; color: var(--white); font-size: 15px;
    padding: 8px 24px; border-radius: 20px; white-space: nowrap;
  }
  .main-nav a.active { background: var(--white); color: var(--ink); }
  .cta-band {
    position: absolute; left: 0; top: 580px; width: 870px; height: 100px;
    background: var(--lime);
    display: flex; align-items: center; justify-content: space-between;
    padding: 0 88px 0 80px;
  }
  .cta-band h2 { font-weight: 400; font-size: 30px; color: var(--ink); white-space: nowrap; }
  .btn-contact {
    background: var(--black); color: var(--white); text-decoration: none;
    font-size: 22px; padding: 6px 30px; border-radius: 4px; white-space: nowrap;
  }
  .band-pointer { position: absolute; left: 415px; top: 680px; }
  .intro-questions {
    position: absolute; top: 722px; left: 0; width: 870px;
    text-align: center; color: var(--lime-text); font-size: 22px; line-height: 1.3;
  }
  .intro-body {
    position: absolute; top: 848px; left: 30px; width: 810px;
    color: var(--body-grey); font-size: 11.2px; line-height: 1.7; text-align: center;
  }
  .intro-body p + p { margin-top: 14px; }
  .btn-visit {
    position: absolute; left: 330px; top: 1040px; width: 210px; height: 50px;
    background: var(--lime); color: var(--ink); text-decoration: none;
    font-size: 24px; border-radius: 4px; white-space: nowrap;
    display: flex; align-items: center; justify-content: center;
  }
  .site-footer {
    position: absolute; left: 0; top: 1160px; width: 870px; height: 40px;
    background: var(--black); color: var(--white);
    display: flex; align-items: center; justify-content: space-between; padding: 0 36px;
    font-size: 10px;
  }
  .social-links { display: flex; gap: 28px; }
  .social-links span { width: 14px; height: 14px; border-radius: 50%; background: var(--white); display: block; }
</style>
</head>
<body>
  <header>
    <div class="hero" role="img" aria-label="Photograph of a smiling family of four, parents with two young children, lying together"></div>
    <div class="brand">
      <span class="brand-dot"></span>
      <span class="brand-name">Meadowgate Counselors</span>
    </div>
    <nav class="main-nav">
      <a class="active" href="#">HOME</a>
      <a href="#">ABOUT</a>
      <a href="#">CONTACT</a>
    </nav>
  </header>

  <section class="cta-band">
    <h2>Feeling stressed and overwhelmed?</h2>
    <a class="btn-contact" href="#">contact us</a>
  </section>
  <svg class="band-pointer" width="40" height="20" viewBox="0 0 40 20"><path d="M0 0 L40 0 L20 20 Z" fill="#b3cb3c"/></svg>

  <section class="intro-questions">
    <p>Feeling stressed and overwhelmed?</p>
    <p>Encountering barriers towards your goals?</p>
    <p>Having difficulty accomplishing the simplest task?</p>
    <p>Have the need to talk but unsure who to turn to?</p>
  </section>

  <section class="intro-body">
    <p>Therapy can assist you in overcoming all of these challenges. Assist you in uncovering the difficulties and barriers that are keeping you from achieving your life’s ambitions, help discover ways to overcome them, and cope with the impact your behaviour has on your occupation, personal life and social life.</p>
    <p>Welcome to our practice, with over 20 years of combined experience in the clinical field you are sure to find the right fit for your needs. Each clinician has experience working with groups, adults, teens, children, families, and couples. We specialize in fostering healthy relationships between individuals, managing depression and anxiety, overcoming trauma, and developing occupational success. Feel free to explore information about each clinician and make an appointment with one of us today.</p>
  </section>

  <a class="btn-visit" href="#">Visit Therapists</a>

  <footer class="site-footer">
    <span>© Meadowgate Counselors - 2015. All Rights Reserved.</span>
    <div class="social-links"><span></span><span></span><span></span></div>
  </footer>
</body>
</html>
```